New business card, letter head, email signature and Portfolio for our Security company.

We are an Elite security company that provides a top quality manpower services to protect high rise buildings, retail and all type of properties and would like a new business card/logo look.

- We would like the spot UV design.
- Matt black (double sided).
- We would like to incorporate a royal blue colour (feel free to experiment with it).
- Feel free to try different lengths with the card to make it stand out more than a normal business card.
- We would like the logo to be an eagle eye in the background (shines when card is tilted slightly in the background, either on the front, back or both sides of the card). Image attached as an example of eye shape (colour to be either black or royal blue).
- MAVRIN OAK GUARD PATROLS PTY. LTD. and MOGP to be placed on one side of the card and on the other side of the card to have;

- Name in slightly bigger font than the position (directly on the bottom on the name).
- Mobile number
- Email address
- Website email address
- PO BOX address

Can we please have the files in a format that we can edit.

Reason: I need to consult my business partner with the designs so far and will make a decision from there.

Target Market(s)

Security Industry

Industry/Entity Type

Business

Contact Information for Business Card

- Mobile number
- Email address
- Website email address
- PO BOX address

Logo Text

MOGP and underneath the MOGP please add MAVRIN OAK GUARD PATROLS PTY. LTD.

Font styles to use
Other font styles liked:
• bold type font

Colors
0255a3
000000

Requirements
Must have
• We are an Elite security company that provides a top quality manpower services to protect high rise buildings, retail and all type of properties and would like a new business card/logo look.
• - We would like the spot UV design.
• - Matt black (double sided).
• - We would like to incorporate a royal blue colour (feel free to experiment with it).
• - Feel free to try different lengths with the card to make it stand out more than a normal business card.
• - We would like the logo to be an eagle eye in the background (shines when card is tilted slightly in the background, either on the front, back or both sides of the card). Image attached as an example of eye shape (colour to be either black or royal blue).
• - MAVRIN OAK GUARD PATROLS PTY. LTD. and MOGP to be placed on one side of the card and on the other side of the card to have;
• - Name in slightly bigger font than the position (directly on the bottom on the name).
• - Mobile number
• - Email address
• - Website email address
• - PO BOX address
• Can we please have the files in a format that we can edit.
Nice to have
• Feel free to try different lengths with the card to make it stand out more than a normal business card.
• Please find "URBAN JUNGLE" font attached and incorporate MOGP into the same style with building's inside the MOGP bold front also add MAVRIN into the bottom part of the S and follow on E - Elite on the bottom S - SECURITY on the bottom S - SERVICES on the bottom of each letter.
• other than that, I'll be happy with a bold modern font for the MOGP and MAVRIN OAK GUARD PATROLS in a bold and thinner font underneath.

```html
<!DOCTYPE html>
<html lang="en">
<head>
<meta charset="utf-8">
<title>Mavrin Oak Guard Patrols – Business Card</title>
<link rel="stylesheet" href="https://fonts.googleapis.com/css2?family=Oswald:wght@500;700&family=Questrial&display=swap">
<style>
  :root {
    --backdrop: #e6e3de;
    --royal-blue: #0255a3;
    --matt-black: #000000;
    --spot-grey: #333333;
    --spot-edge: #454545;
    --white: #ffffff;
    --soft-white: #e8e8e8;
  }
  html, body {
    margin: 0;
    width: 1200px;
    height: 400px;
    overflow: hidden;
    background: var(--backdrop);
  }
  .canvas {
    position: relative;
    width: 1200px;
    height: 400px;
  }
  .card {
    position: absolute;
    top: 93px;
    width: 479px;
    height: 213px;
    overflow: hidden;
  }
  .card--front {
    left: 109px;
    background: var(--royal-blue);
  }
  .card--back {
    left: 611px;
    background: var(--matt-black);
  }
  .front-mark {
    position: absolute;
    left: 0;
    right: 0;
    top: 70px;
    text-align: center;
    font-family: "Oswald", sans-serif;
    font-weight: 700;
    font-size: 52px;
    line-height: 1;
    color: var(--white);
    letter-spacing: 2px;
  }
  .front-name {
    position: absolute;
    left: 0;
    right: 0;
    top: 166px;
    text-align: center;
    font-family: "Oswald", sans-serif;
    font-weight: 500;
    font-size: 15px;
    line-height: 1;
    color: var(--white);
    letter-spacing: 0.2px;
  }
  .spot-uv-panel {
    position: absolute;
    left: 0;
    top: 0;
    width: 140px;
    height: 213px;
  }
  .back-brand {
    position: absolute;
    left: 221px;
    top: 22px;
    width: 154px;
    text-align: center;
  }
  .back-brand__mark {
    font-family: "Oswald", sans-serif;
    font-weight: 700;
    font-size: 60px;
    line-height: 1;
    color: var(--white);
    letter-spacing: 1px;
  }
  .back-brand__name {
    margin-top: 6px;
    font-family: "Oswald", sans-serif;
    font-weight: 500;
    font-size: 9.5px;
    line-height: 1;
    color: var(--white);
    letter-spacing: 0.3px;
    white-space: nowrap;
  }
  .contact {
    position: absolute;
    left: 220px;
    top: 116px;
    font-family: "Questrial", sans-serif;
    color: var(--soft-white);
  }
  .contact__person {
    font-size: 13px;
    line-height: 16px;
    color: var(--white);
    letter-spacing: 0.2px;
    margin-bottom: 1px;
  }
  .contact__list {
    list-style: none;
    margin: 0;
    padding: 0;
  }
  .contact__item {
    display: flex;
    align-items: center;
    height: 16px;
    font-size: 12.5px;
    letter-spacing: 0.2px;
    white-space: nowrap;
  }
  .contact__icon {
    width: 8px;
    height: 8px;
    margin: 0 7px 0 6px;
    flex: none;
  }
  .contact__item--plain {
    padding-left: 21px;
  }
</style>
</head>
<body>
<main class="canvas">
  <section class="card card--front" aria-label="Card front">
    <div class="front-mark">MOGP</div>
    <div class="front-name">MAVRIN OAK GUARD PATROLS</div>
  </section>

  <section class="card card--back" aria-label="Card back">
    <svg class="spot-uv-panel" viewBox="0 0 140 213" role="img" aria-label="Spot UV eagle eye decoration area">
      <defs>
        <linearGradient id="spot-fill" x1="0" y1="0" x2="1" y2="0">
          <stop offset="0" stop-color="#383838"/>
          <stop offset="1" stop-color="#2e2e2e"/>
        </linearGradient>
      </defs>
      <path d="M0 0 H130 C133 80 126 160 68 213 H0 Z" fill="url(#spot-fill)"/>
      <path d="M130 0 C133 80 126 160 68 213" fill="none" stroke="var(--spot-edge)" stroke-width="2"/>
    </svg>

    <div class="back-brand">
      <div class="back-brand__mark">MOGP</div>
      <div class="back-brand__name">MAVRIN OAK GUARD PATROLS</div>
    </div>

    <div class="contact">
      <div class="contact__person">JORDAN VALE</div>
      <ul class="contact__list">
        <li class="contact__item">
          <svg class="contact__icon" viewBox="0 0 8 8" aria-hidden="true"><rect width="8" height="8" rx="1" fill="#0255a3"/><path d="M2.5 2 L3.5 2 L3.5 6 L5.5 6" stroke="#fff" stroke-width="1" fill="none"/></svg>
          MOBILE NUMBER
        </li>
        <li class="contact__item">
          <svg class="contact__icon" viewBox="0 0 8 8" aria-hidden="true"><rect width="8" height="8" rx="1" fill="#0255a3"/><rect x="1.8" y="2.5" width="4.4" height="3" fill="none" stroke="#fff" stroke-width="0.8"/></svg>
          EMAIL ADDRESS
        </li>
        <li class="contact__item">
          <svg class="contact__icon" viewBox="0 0 8 8" aria-hidden="true"><rect width="8" height="8" rx="1" fill="#0255a3"/><circle cx="4" cy="4" r="2" fill="none" stroke="#fff" stroke-width="0.8"/></svg>
          WEBSITE EMAIL ADDRESS
        </li>
        <li class="contact__item contact__item--plain">PO BOX ADDRESS</li>
      </ul>
    </div>
  </section>
</main>
</body>
</html>
```